Dorsey K. Wendell Business Card

We need a business card for our company Dorsey K. Wendell Heating & Plumbing to be distributed to potential customers. It should follow the color scheme of our logo and have a modern upscale and masculine look.

The logo is attached and the info below should also be included:

5187 W. Cedar Brook Rd.
Halloway, PA 17638

Russell T. Wendell
(717) 592-0817
russelltwendell@fernmail.net
dorseykwendell.net
PA #093148

Industry/Entity Type

Business

Contact Information for Business Card

5187 W. Cedar Brook Rd.
Halloway, PA 17638

Russell T. Wendell
(717) 592-0817
russelltwendell@fernmail.net
dorseykwendell.net
PA #093148

Colors

Designer to choose colors to be used in the design.

Requirements
Must have
• Information above included

```html
<!DOCTYPE html>
<html lang="en">
<head>
<meta charset="utf-8">
<title>Dorsey K. Wendell Business Card</title>
<link href="https://fonts.googleapis.com/css2?family=Archivo:wght@800&family=Open+Sans:wght@400;600&display=swap" rel="stylesheet">
<style>
  :root {
    --lime: #a9d13a;
    --royal: #0a55a5;
    --paper: #ffffff;
    --ink: #2a2a2a;
    --backdrop: #e9e6e1;
  }
  * { box-sizing: border-box; margin: 0; padding: 0; }
  html, body { width: 1200px; height: 880px; overflow: hidden; }
  body {
    background: var(--backdrop);
    position: relative;
    font-family: "Open Sans", sans-serif;
  }
  .card {
    position: absolute;
    width: 620px;
    height: 354px;
    box-shadow: 0 6px 18px rgba(0,0,0,0.18);
    overflow: hidden;
  }

  /* Front */
  .card-front { left: 70px; top: 50px; background: var(--lime); }
  .front-brand {
    position: absolute; left: 0; right: 0; top: 110px;
    display: flex; align-items: center; justify-content: center; gap: 18px;
  }
  .brand-square { width: 58px; height: 58px; background: var(--royal); flex: none; }
  .front-brand .brand-name {
    font-family: "Archivo", sans-serif; font-weight: 800;
    color: var(--royal); font-size: 34px; letter-spacing: 1px; text-transform: uppercase;
  }
  .front-web {
    position: absolute; left: 0; right: 0; bottom: 44px; text-align: center;
    font-size: 15px; letter-spacing: 5px; color: var(--ink);
  }

  /* Back */
  .card-back { left: 510px; top: 476px; background: var(--paper); }
  .back-brand {
    position: absolute; left: 36px; top: 44px;
    display: flex; align-items: center; gap: 12px;
  }
  .back-brand .brand-square { width: 42px; height: 42px; }
  .back-brand .brand-name {
    font-family: "Archivo", sans-serif; font-weight: 800;
    color: var(--royal); font-size: 19px; line-height: 1.15; text-transform: uppercase;
  }
  .contact-band {
    position: absolute; left: 292px; top: 100px; width: 328px; height: 122px;
    background: var(--royal); color: #fff; padding: 12px 0 0 44px;
    font-size: 14px; line-height: 24px;
  }
  .contact-line { display: flex; align-items: center; gap: 8px; }
  .contact-line svg { width: 13px; height: 13px; flex: none; }
  .contact-line.license { padding-left: 21px; }
  .name-band {
    position: absolute; left: 0; top: 222px; width: 386px; height: 62px;
    background: var(--lime);
    display: flex; align-items: center; padding-left: 40px;
  }
  .holder-name {
    font-family: "Archivo", sans-serif; font-weight: 800;
    color: var(--royal); font-size: 24px; text-transform: uppercase; letter-spacing: 0.5px;
  }
  .address {
    position: absolute; left: 40px; top: 294px;
    font-size: 17px; line-height: 24px; color: var(--ink);
  }
</style>
</head>
<body>
  <section class="card card-front">
    <div class="front-brand">
      <span class="brand-square"></span>
      <span class="brand-name">Dorsey K. Wendell</span>
    </div>
    <p class="front-web">www.dorseykwendell.net</p>
  </section>

  <section class="card card-back">
    <div class="back-brand">
      <span class="brand-square"></span>
      <span class="brand-name">Dorsey K. Wendell<br>Heating &amp; Plumbing</span>
    </div>

    <div class="contact-band">
      <p class="contact-line">
        <svg viewBox="0 0 16 16"><circle cx="8" cy="8" r="7" fill="none" stroke="#fff" stroke-width="1.5"/><path d="M5.5 4.5l1.5 0 .6 2-1 .8a5 5 0 0 0 2.1 2.1l.8-1 2 .6v1.5c-3.5.3-6.3-2.5-6-6z" fill="#fff"/></svg>
        (717) 592-0817
      </p>
      <p class="contact-line">
        <svg viewBox="0 0 16 16"><rect x="1.5" y="4" width="13" height="9" fill="#fff"/><path d="M1.5 4l6.5 5 6.5-5" fill="none" stroke="#0a55a5" stroke-width="1.3"/></svg>
        russelltwendell@fernmail.net
      </p>
      <p class="contact-line">
        <svg viewBox="0 0 16 16" fill="none" stroke="#fff" stroke-width="1.3"><circle cx="8" cy="8" r="6.5"/><ellipse cx="8" cy="8" rx="3" ry="6.5"/><path d="M1.5 8h13M2.5 4.8h11M2.5 11.2h11"/></svg>
        www.dorseykwendell.net
      </p>
      <p class="contact-line license">PA #093148</p>
    </div>

    <div class="name-band">
      <h1 class="holder-name">Russell T. Wendell</h1>
    </div>

    <p class="address">5187 W. Cedar Brook Rd.<br>Halloway, PA 17638</p>
  </section>
</body>
</html>
```